BRCW Business Cards

Business Cards should contain:
Bright Ridgecrest Coating Works
Felix Darrow
M: 0417 865 093
E: brightRCW@fernpost.example
BRCW logo
TCG logo
Painting & Decorating
Licence # 719362K
slogan: see the craft of lasting brilliance

Target Market(s)

all aspect of painting

Industry/Entity Type

Trade

Contact Information for Business Card

Felix Darrow
M: 0417 865 093
E: brightRCW@fernpost.example
BRCW logo
TCG logo
Painting & Decorating
Licence # 719362K

Font styles to use
Serif
Sans Serif

Requirements
Must have
• clear design with nice backround
• two sides
• smal TCG logo
Nice to have
• easy to read
Should not have
• mess
• black
• plastics form

```html
<!DOCTYPE html>
<html lang="en">
<head>
<meta charset="utf-8">
<title>BRCW Business Cards</title>
<link href="https://fonts.googleapis.com/css2?family=Crimson+Pro:wght@500;600&family=Libre+Caslon+Text:wght@400&family=Lato:ital,wght@0,400;1,400&family=Montserrat:wght@700&display=swap" rel="stylesheet">
<style>
  :root {
    --backdrop: #d1d2d4;
    --card: #ffffff;
    --deep-teal: #134f4f;
    --leaf-green: #3b8b3f;
    --band-teal: #22a28c;
    --accent-orange: #f05a28;
    --text-dark: #1f3a3a;
    --partner-blue: #1f4ea3;
    --faint-mark: #f3f3f3;
  }
  * { margin: 0; padding: 0; box-sizing: border-box; }
  html, body { width: 962px; height: 1200px; overflow: hidden; background: var(--backdrop); }
  .canvas { position: relative; width: 962px; height: 1200px; }
  .card {
    position: absolute; left: 108px; width: 746px; height: 456px;
    background: var(--card); border-radius: 38px;
    box-shadow: 0 4px 14px rgba(0,0,0,0.12); overflow: hidden;
  }
  .card--front { top: 108px; }
  .card--back { top: 636px; }

  /* front */
  .faint-name {
    position: absolute; left: 28px; top: 100px;
    font-family: "Libre Caslon Text", serif; font-size: 110px; line-height: 1;
    color: var(--faint-mark);
  }
  .brand-mark {
    position: absolute; left: 274px; top: 150px; width: 110px; height: 206px;
    background: linear-gradient(180deg, #3b8b3f 0%, #22a28c 40%, #134f4f 100%);
    border-radius: 10px;
  }
  .brand-divider {
    position: absolute; left: 402px; top: 150px; width: 2px; height: 204px;
    background: var(--deep-teal);
  }
  .brand-initials {
    position: absolute; left: 418px; top: 160px;
    font-family: "Libre Caslon Text", serif; font-size: 90px; line-height: 1;
    color: var(--deep-teal); letter-spacing: 1px;
  }
  .brand-name {
    position: absolute; left: 420px; top: 262px; width: 286px; text-align: right;
    font-family: "Crimson Pro", serif; font-weight: 600; font-size: 36px; line-height: 44px;
    letter-spacing: -0.5px;
  }
  .brand-name__top { display: block; color: var(--leaf-green); }
  .brand-name__bottom { display: block; color: var(--deep-teal); }
  .service-band {
    position: absolute; left: 276px; top: 371px; width: 427px; height: 31px;
    background: var(--band-teal); border-radius: 16px;
    font-family: "Montserrat", sans-serif; font-weight: 700; font-size: 17px;
    color: #fff; letter-spacing: 1.2px; text-align: center; line-height: 31px;
  }
  .slogan {
    position: absolute; left: 276px; top: 406px; width: 427px; text-align: center;
    font-family: "Lato", sans-serif; font-style: italic; font-size: 18px;
    color: var(--accent-orange); letter-spacing: 0.6px;
  }

  /* back */
  .back-mark {
    position: absolute; left: 30px; top: 120px; width: 290px; text-align: center;
    font-family: "Libre Caslon Text", serif; font-size: 76px; line-height: 1;
    color: var(--deep-teal);
  }
  .contact { position: absolute; left: 372px; top: 154px; font-family: "Lato", sans-serif; }
  .contact__name {
    font-family: "Montserrat", sans-serif; font-weight: 700; font-size: 27px;
    color: var(--band-teal); letter-spacing: 0.8px; line-height: 1; margin-bottom: 20px;
  }
  .contact__line { font-size: 22px; color: var(--text-dark); letter-spacing: 0.6px; line-height: 32px; }
  .contact__label { color: var(--accent-orange); }
  .contact__licence { font-size: 17px; color: var(--text-dark); margin-top: 16px; letter-spacing: 0.3px; }
  .partner {
    position: absolute; left: 628px; top: 380px;
    font-family: "Montserrat", sans-serif; font-weight: 700; font-size: 28px;
    color: var(--partner-blue); letter-spacing: 0.5px;
  }
</style>
</head>
<body>
<main class="canvas">
  <section class="card card--front" aria-label="Card front">
    <div class="faint-name" aria-hidden="true">BRCW</div>
    <div class="brand-mark" role="img" aria-label="BRCW logo mark"></div>
    <div class="brand-divider"></div>
    <div class="brand-initials">BRCW</div>
    <h1 class="brand-name">
      <span class="brand-name__top">Bright Ridgecrest</span>
      <span class="brand-name__bottom">Coating Works</span>
    </h1>
    <div class="service-band">PAINTING &amp; DECORATING</div>
    <p class="slogan">see the craft of lasting brilliance</p>
  </section>

  <section class="card card--back" aria-label="Card back">
    <div class="back-mark">BRCW</div>
    <div class="contact">
      <h2 class="contact__name">FELIX DARROW</h2>
      <p class="contact__line"><span class="contact__label">m:</span> 0417 865 093</p>
      <p class="contact__line"><span class="contact__label">e:</span> brightRCW@fernpost.example</p>
      <p class="contact__licence">Licence #: 719362K</p>
    </div>
    <div class="partner">TCG</div>
  </section>
</main>
</body>
</html>
```